Modern Yoga Studio Timetable and Flyer Design

We have a comprehensive class timetable and we are wanting to a clean modern look for our Spring timetable.

We require a double sided flyer with our class timetable included.
We would prefer an A5 size (postcard) or DL (1/3 A4).

We would like the final flyer to have.
Side A : Yoga image, logo

Fennel Stretch Hall
address: 4/71 Wexcombe Lane, Pelharton
website: fennelstretch.com.au
mobile: 0471 296 814

Side B: Clear easy to read timetable with a break down of class types and website.

We would also like to have a copy of the timetable itself as a separate jpg or pdf for use on our website to download.

Thank you.
Yours kindly,
Nell

I have attached a sample of another timetable of which I like the look and feel of, however this is just a guide. I've also attached our 'new' schedule in WORD plus uploaded our last design of the front.
Updates

Target Market(s)

Women aged 30-45

Industry/Entity Type

Health And Wellness

Font styles to use
Other font styles liked:
• Brandon Grotesque, Jenna Sue

Colors
6c459b
33a6d7
ffffff

Requirements
Must have
• A definitive colour to decipher between different class types on our timetable. Where each colour represents a different class type. Colours and layouts similar to our website design, see www.fennelstretch.com.au
Nice to have
• I've included a design of another studio whose timetable design I like. One of our own yoga images instead of a stock image.
Should not have
• No dark gridlines between the cells/boxes in the timetables. Please don't use stock yoga images.

```html
<!DOCTYPE html>
<html lang="en">
<head>
<meta charset="utf-8">
<title>Fennel Stretch Hall – Spring Timetable Flyer</title>
<link href="https://fonts.googleapis.com/css2?family=Josefin+Sans:wght@400;600;700&display=swap" rel="stylesheet">
<style>
  :root{
    --backdrop:#bca6b7;
    --paper:#f7f7f7;
    --ink:#4a4a4a;
    --ink-soft:#7a7a7a;
    --brand-blue:#33a6d7;
    --c-slow:#b7a3cf;
    --c-preg:#b5d98a;
    --c-vinyasa:#eda68c;
    --c-rise:#cdcdcd;
    --c-mum:#8ecbe3;
    --c-kids812:#f4c48e;
    --c-teens:#cc8fbd;
    --c-yinrest:#d5bfac;
    --c-kids57:#d9e47c;
    --c-women:#8fd5ae;
    --c-flow:#f0e486;
    --c-yin:#ed8bbf;
    --photo-wall:#f1efec;
    --photo-floor:#a9794a;
  }
  *{box-sizing:border-box;margin:0;padding:0}
  html,body{width:1200px;height:900px;overflow:hidden}
  body{background:var(--backdrop);font-family:"Josefin Sans",sans-serif;position:relative}
  .flyer{position:absolute;left:305px;width:590px;height:417px;background:var(--paper);box-shadow:0 6px 18px rgba(60,30,60,.18);overflow:hidden}
  .flyer--timetable{top:22px}
  .flyer--front{top:461px}
  .timetable{display:block;width:100%;height:100%}
  .day{font-weight:700;font-size:13px;fill:var(--ink);letter-spacing:.5px}
  .class-name{font-weight:700;font-size:10px;fill:#fff;text-anchor:middle;letter-spacing:.3px}
  .class-mark{font-weight:700;font-size:9px;fill:#fff;text-anchor:middle}
  .time{font-weight:700;font-size:9px;letter-spacing:.2px}
  .time--small{font-size:6.5px}
  .note{font-size:9px;fill:var(--ink-soft);letter-spacing:.3px}
  .site{font-size:10px;fill:var(--ink);letter-spacing:.3px}
  .photo{position:absolute;inset:0;background:linear-gradient(180deg,var(--photo-wall) 0%,#e9e6e2 52%,#b88956 60%,var(--photo-floor) 100%)}
  .brand{position:absolute;top:18px;right:22px;display:flex;align-items:center;gap:8px}
  .brand__dot{width:14px;height:14px;border-radius:50%;background:var(--brand-blue)}
  .brand__name{font-weight:600;font-size:18px;color:var(--brand-blue);letter-spacing:.5px}
  .contact{position:absolute;left:24px;bottom:20px;color:#fff;font-size:12px;letter-spacing:.6px;display:flex;gap:10px}
  .contact__sep{opacity:.8}
</style>
</head>
<body>

<section class="flyer flyer--timetable" aria-label="Class timetable">
  <svg class="timetable" viewBox="0 0 590 417" xmlns="http://www.w3.org/2000/svg">
    <!-- days -->
    <g class="days">
      <text class="day" x="18" y="174">MON</text>
      <text class="day" x="18" y="204">TUE</text>
      <text class="day" x="18" y="234">WED</text>
      <text class="day" x="18" y="264">THU</text>
      <text class="day" x="18" y="294">FRI</text>
      <text class="day" x="18" y="324">SAT</text>
      <text class="day" x="18" y="354">SUN</text>
    </g>

    <!-- stems -->
    <g class="stems" stroke-width="2.5" stroke-linecap="round">
      <line x1="80" y1="86" x2="80" y2="372" stroke="var(--c-slow)"/>
      <line x1="122" y1="136" x2="122" y2="372" stroke="var(--c-preg)"/>
      <line x1="164" y1="86" x2="164" y2="372" stroke="var(--c-vinyasa)"/>
      <line x1="206" y1="136" x2="206" y2="372" stroke="var(--c-rise)"/>
      <line x1="248" y1="86" x2="248" y2="372" stroke="var(--c-mum)"/>
      <line x1="290" y1="136" x2="290" y2="372" stroke="var(--c-kids812)"/>
      <line x1="332" y1="86" x2="332" y2="372" stroke="var(--c-teens)"/>
      <line x1="374" y1="136" x2="374" y2="372" stroke="var(--c-yinrest)"/>
      <line x1="416" y1="86" x2="416" y2="372" stroke="var(--c-kids57)"/>
      <line x1="458" y1="136" x2="458" y2="372" stroke="var(--c-women)"/>
      <line x1="500" y1="86" x2="500" y2="372" stroke="var(--c-flow)"/>
      <line x1="542" y1="136" x2="542" y2="372" stroke="var(--c-yin)"/>
    </g>

    <!-- class bubbles -->
    <g class="bubbles">
      <circle cx="80" cy="58" r="29" fill="var(--c-slow)"/>
      <text class="class-name" x="80" y="56">SLOW</text><text class="class-name" x="80" y="68">FLOW</text>

      <circle cx="122" cy="108" r="29" fill="var(--c-preg)"/>
      <text class="class-mark" x="122" y="100">*</text><text class="class-name" x="122" y="112" style="font-size:8px">PREGNANCY</text>

      <circle cx="164" cy="58" r="29" fill="var(--c-vinyasa)"/>
      <text class="class-name" x="164" y="56">VINYASA</text><text class="class-name" x="164" y="68">FLOW</text>

      <circle cx="206" cy="108" r="29" fill="var(--c-rise)"/>
      <text class="class-mark" x="206" y="93">*</text><text class="class-name" x="206" y="104">RISE</text><text class="class-mark" x="206" y="113">+</text><text class="class-name" x="206" y="123">SHINE</text>

      <circle cx="248" cy="58" r="29" fill="var(--c-mum)"/>
      <text class="class-mark" x="248" y="43">*</text><text class="class-name" x="248" y="54">MUM</text><text class="class-mark" x="248" y="63">+</text><text class="class-name" x="248" y="73">BABY</text>

      <circle cx="290" cy="108" r="29" fill="var(--c-kids812)"/>
      <text class="class-mark" x="290" y="96">*</text><text class="class-name" x="290" y="108">KIDS</text><text class="class-name" x="290" y="120">8-12</text>

      <circle cx="332" cy="58" r="29" fill="var(--c-teens)"/>
      <text class="class-mark" x="332" y="46">*</text><text class="class-name" x="332" y="58">TEENS</text><text class="class-name" x="332" y="70">12-16</text>

      <circle cx="374" cy="108" r="29" fill="var(--c-yinrest)"/>
      <text class="class-name" x="374" y="104">YIN</text><text class="class-mark" x="374" y="112">+</text><text class="class-name" x="374" y="122" style="font-size:8.5px">RESTORE</text>

      <circle cx="416" cy="58" r="29" fill="var(--c-kids57)"/>
      <text class="class-mark" x="416" y="46">*</text><text class="class-name" x="416" y="58">KIDS</text><text class="class-name" x="416" y="70">5-7</text>

      <circle cx="458" cy="108" r="29" fill="var(--c-women)"/>
      <text class="class-mark" x="458" y="96">*</text><text class="class-name" x="458" y="108" style="font-size:8.5px">WOMEN'S</text><text class="class-name" x="458" y="119" style="font-size:8.5px">WELLNESS</text>

      <circle cx="500" cy="58" r="29" fill="var(--c-flow)"/>
      <text class="class-name" x="500" y="54">FLOW</text><text class="class-mark" x="500" y="62">+</text><text class="class-name" x="500" y="72" style="font-size:8.5px">RESTORE</text>

      <circle cx="542" cy="108" r="29" fill="var(--c-yin)"/>
      <text class="class-name" x="542" y="112" style="font-size:12px">YIN</text>
    </g>

    <!-- session times -->
    <g class="times">
      <g fill="var(--c-slow)">
        <text class="time" x="84" y="166">9:30</text><text class="time" x="84" y="174">AM</text>
        <text class="time" x="84" y="226">6:00</text><text class="time" x="84" y="234">PM</text>
      </g>
      <g fill="var(--c-preg)">
        <text class="time" x="126" y="166">6:00</text><text class="time" x="126" y="174">PM</text>
        <text class="time" x="126" y="196">7:30</text><text class="time" x="126" y="204">PM</text>
        <text class="time time--small" x="126" y="258">12:15PM</text><text class="time time--small" x="126" y="265">6:15PM</text>
        <text class="time" x="126" y="316">10:30</text><text class="time" x="126" y="324">AM</text>
      </g>
      <g fill="var(--c-vinyasa)">
        <text class="time" x="168" y="166">7:30</text><text class="time" x="168" y="174">PM</text>
        <text class="time time--small" x="168" y="198">9:15AM</text><text class="time time--small" x="168" y="205">6:00PM</text>
        <text class="time" x="168" y="256">9:30</text><text class="time" x="168" y="264">AM</text>
        <text class="time time--small" x="168" y="318">9:00AM</text><text class="time time--small" x="168" y="325">4:00PM</text>
      </g>
      <g fill="var(--c-rise)">
        <text class="time" x="210" y="196">5:45</text><text class="time" x="210" y="204">AM</text>
        <text class="time" x="210" y="256">5:45</text><text class="time" x="210" y="264">AM</text>
      </g>
      <g fill="var(--c-mum)">
        <text class="time" x="252" y="196">11:00</text><text class="time" x="252" y="204">AM</text>
        <text class="time" x="252" y="256">11:00</text><text class="time" x="252" y="264">AM</text>
      </g>
      <g fill="var(--c-kids812)">
        <text class="time" x="294" y="226">4:00</text><text class="time" x="294" y="234">PM</text>
      </g>
      <g fill="var(--c-teens)">
        <text class="time" x="336" y="226">4:45</text><text class="time" x="336" y="234">PM</text>
        <text class="time" x="336" y="256">5:00</text><text class="time" x="336" y="264">PM</text>
      </g>
      <g fill="var(--c-yinrest)">
        <text class="time" x="378" y="226">7:30</text><text class="time" x="378" y="234">PM</text>
      </g>
      <g fill="var(--c-kids57)">
        <text class="time" x="420" y="256">4:00</text><text class="time" x="420" y="264">PM</text>
      </g>
      <g fill="var(--c-women)">
        <text class="time" x="462" y="256">7:30</text><text class="time" x="462" y="264">PM</text>
      </g>
      <g fill="var(--c-flow)">
        <text class="time" x="504" y="286">6:00</text><text class="time" x="504" y="294">PM</text>
      </g>
      <g fill="var(--c-yin)">
        <text class="time" x="546" y="346">9:15</text><text class="time" x="546" y="354">AM</text>
      </g>
    </g>

    <text class="note" x="18" y="398">*BOOKINGS ESSENTIAL</text>
    <text class="site" x="572" y="400" text-anchor="end">www.fennelstretch.com.au</text>
  </svg>
</section>

<section class="flyer flyer--front" aria-label="Flyer front">
  <div class="photo" role="img" aria-label="Photograph of two women in purple tops holding yoga poses on a woven mat against a pale wall"></div>
  <div class="brand">
    <span class="brand__dot"></span>
    <span class="brand__name">Fennel Stretch Hall</span>
  </div>
  <p class="contact">
    <span>4/71 Wexcombe Lane, Pelharton</span>
    <span class="contact__sep">/</span>
    <span>www.fennelstretch.com.au</span>
    <span class="contact__sep">/</span>
    <span>0471 296 814</span>
  </p>
</section>

</body>
</html>
```